Fancy looking Inspection Postcard

Postcard needed for customers to inspect their product once it is delivered. We'll be giving them the steps for inspecting their product and to contact us if any issues arise. Would like to see something that sticks out but uses our company's colors. Would like to see creativity. Possibly utilizing the diamond steel background like we have in our logo.

Target Market(s)

Customers of our manufacturing shop

Industry/Entity Type

Manufacturing - metal wall art, custom products

Requirements
Must have
• our colors and logo
Nice to have
• get creative. i like creativity

```html
<!DOCTYPE html>
<html lang="en">
<head>
<meta charset="utf-8">
<title>Bitter Creek Fabrication – Product Checklist Postcard</title>
<link href="https://fonts.googleapis.com/css2?family=Montserrat:wght@800;900&family=Nunito:ital,wght@0,700;0,800;0,900;1,900&display=swap" rel="stylesheet">
<style>
  :root {
    --stage: #3d3d3d;
    --brand-yellow: #ffec00;
    --panel-black: #0f0e0b;
    --ink: #111111;
    --white: #ffffff;
  }
  * { margin: 0; padding: 0; box-sizing: border-box; }
  html, body { width: 1200px; height: 1200px; overflow: hidden; background: var(--stage); }
  body { position: relative; font-family: "Nunito", sans-serif; }

  .postcard {
    position: absolute; left: 271px; top: 107px;
    width: 657px; height: 985px;
    background: var(--brand-yellow);
    box-shadow: 0 20px 50px rgba(0,0,0,.45);
  }
  .checklist-panel {
    position: absolute; left: 10px; top: 10px;
    width: 638px; height: 717px;
    background: var(--panel-black);
    overflow: hidden;
  }

  .panel-title {
    position: absolute; left: 0; top: 0;
    width: 638px; height: 717px;
  }
  .title-word {
    font-family: "Montserrat", sans-serif; font-weight: 900;
    font-size: 63px;
    fill: var(--brand-yellow);
  }

  .step { position: absolute; left: 0; width: 657px; }
  .step-heading {
    position: absolute; left: 280px; top: -17px;
    font-weight: 900; font-size: 27px; line-height: 34px;
    color: var(--brand-yellow);
  }
  .step-subtitle {
    position: absolute; left: 280px; top: 22px;
    font-weight: 900; font-style: italic; font-size: 16.5px; line-height: 22px;
    color: var(--white); text-transform: uppercase; letter-spacing: -.2px;
  }
  .step-rule {
    position: absolute; left: 243px; right: 19px; top: 51px;
    height: 1.5px; background: var(--brand-yellow);
  }
  .check-item {
    position: absolute; left: 243px;
    display: flex; align-items: center; height: 20px;
    font-weight: 700; font-size: 17px; color: var(--white);
  }
  .check-box { width: 16px; height: 16px; background: var(--white); margin-right: 21px; flex: none; }
  .item-one { top: 65px; }
  .item-two { top: 92px; }
  .step.offset .step-heading, .step.offset .step-subtitle { left: 283px; }
  .step.offset .check-box { margin-right: 24px; }

  .contact-footer { position: absolute; left: 0; top: 727px; width: 657px; height: 258px; }
  .brand-name {
    position: absolute; left: 38px; top: 76px; width: 168px;
    display: flex; align-items: center; gap: 8px;
    font-weight: 900; font-size: 21px; line-height: 1.1; color: var(--ink);
  }
  .brand-square { width: 16px; height: 16px; background: var(--ink); flex: none; }
  .footer-divider { position: absolute; left: 242px; top: 37px; width: 2px; height: 178px; background: var(--ink); }
  .footer-text {
    position: absolute; left: 284px;
    font-weight: 800; font-size: 13.5px; line-height: 16.5px; color: var(--ink);
  }
  .footer-text a { color: var(--ink); text-decoration: underline; }
  .contact-lines { top: 31px; }
  .review-heading { top: 119px; font-weight: 900; font-style: italic; font-size: 14.5px; }
  .review-heading .stars { font-style: normal; letter-spacing: 1px; margin-right: 6px; }
  .footer-rule { position: absolute; left: 284px; right: 0; height: 1.5px; background: var(--ink); }
  .rule-upper { top: 136px; }
  .rule-lower { top: 180px; }
  .review-ask { top: 156px; }
  .review-issue { top: 189px; }
</style>
</head>
<body>
<main class="postcard">
  <section class="checklist-panel">
    <svg class="panel-title" viewBox="0 0 638 717" aria-labelledby="panel-title-text">
      <title id="panel-title-text">Product Checklist</title>
      <text class="title-word" transform="translate(106 638) rotate(-90)" textLength="289" lengthAdjust="spacingAndGlyphs">PRODUCT</text>
      <text class="title-word" transform="translate(161 456) rotate(-90)" textLength="317" lengthAdjust="spacingAndGlyphs">CHECKLIST</text>
    </svg>

    <div class="step" style="top:89px">
      <h2 class="step-heading">Step 1.</h2>
      <p class="step-subtitle">Inspect general shape</p>
      <div class="step-rule"></div>
      <div class="check-item item-one"><span class="check-box"></span>Is it what you expected?</div>
      <div class="check-item item-two"><span class="check-box"></span>Is it bent, disoriented?</div>
    </div>

    <div class="step" style="top:261px">
      <h2 class="step-heading">Step 2.</h2>
      <p class="step-subtitle">Inspect the welds if there are any</p>
      <div class="step-rule"></div>
      <div class="check-item item-one"><span class="check-box"></span>Do they look clean?</div>
      <div class="check-item item-two"><span class="check-box"></span>Are there any gaps?</div>
    </div>

    <div class="step offset" style="top:413px">
      <h2 class="step-heading">Step 3.</h2>
      <p class="step-subtitle">Inspect the finish</p>
      <div class="step-rule"></div>
      <div class="check-item item-one"><span class="check-box"></span>Are there any areas not finished?</div>
      <div class="check-item item-two"><span class="check-box"></span>Are the colors what you expected?</div>
    </div>

    <div class="step offset" style="top:565px">
      <h2 class="step-heading">Step 4.</h2>
      <p class="step-subtitle">Check for functionality</p>
      <div class="step-rule"></div>
      <div class="check-item item-one"><span class="check-box"></span>Does it work the way you want it to</div>
      <div class="check-item item-two"><span class="check-box"></span>Is it what you expected?</div>
    </div>
  </section>

  <footer class="contact-footer">
    <div class="brand-name"><span class="brand-square"></span><span>BITTER CREEK FABRICATION</span></div>
    <div class="footer-divider"></div>
    <p class="footer-text contact-lines">
      Email us at <a href="mailto:orders@bittercreekfab.com">orders@bittercreekfab.com</a>,<br>
      shoot us a text <a href="tel:5552040144">(555) 204-0144</a>,<br>
      or reach out via <a href="#">www.bittercreekfab.com/contact</a>
    </p>
    <p class="footer-text review-heading"><span class="stars">★★★★★</span>DID WE DO A GOOD JOB?</p>
    <div class="footer-rule rule-upper"></div>
    <p class="footer-text review-ask">If you think so, leave us a review on Searchly?</p>
    <div class="footer-rule rule-lower"></div>
    <p class="footer-text review-issue">If not, Please let us know — info@bittercreekfab.com<br>or call us 555-476-0107</p>
  </footer>
</main>
</body>
</html>
```